New Flyer Design Project

I would like to purchase a customized version of a design you have previously submitted - https://www.plorvania.com/design/58204719

I want this to be something that looks really good.
We use this to explain our service agreements.
our website is www.bqumesh.net I want to stick with those colors.

```html
<!DOCTYPE html>
<html lang="en">
<head>
<meta charset="utf-8">
<title>BQM Support Plans</title>
<link rel="stylesheet" href="https://fonts.googleapis.com/css2?family=Manrope:wght@500;600;700;800&family=Roboto:wght@700&display=swap">
<style>
:root{
  --brand-red:#9b2424;
  --brand-grey:#6d6e72;
  --tick-grey:#5e5f63;
  --ink:#1c1c1c;
  --rule:#8a8b8e;
  --panel-edge:#9a9b9e;
  --page:#8a9093;
  --sheet:#ffffff;
}
*{box-sizing:border-box;margin:0;padding:0}
html,body{width:1200px;height:1200px;overflow:hidden}
body{background:var(--page);font-family:"Manrope",sans-serif;color:var(--ink);position:relative}
.sheet{position:absolute;left:0;top:136px;width:1200px;height:928px;background:var(--sheet)}
.brand{position:absolute;left:61px;top:58px;display:flex;align-items:center;gap:10px}
.brand-dot{width:26px;height:26px;border-radius:50%;background:var(--brand-red)}
.brand-name{font-weight:800;font-size:40px;color:var(--brand-grey);letter-spacing:1px;line-height:1}
.brand-tag{position:absolute;left:61px;top:104px;font-weight:700;font-size:13px;color:var(--brand-red)}
.title{position:absolute;left:559px;top:48px;display:flex;align-items:center;gap:11px}
.title-box{width:212px;height:70px;background:var(--brand-grey);color:#fff;font-family:"Roboto",sans-serif;font-weight:700;font-size:54px;display:flex;align-items:center;justify-content:center;letter-spacing:4px}
.title-text{font-family:"Roboto",sans-serif;font-weight:700;font-size:45px;color:var(--brand-red);letter-spacing:-.5px}
.title-rule{position:absolute;left:559px;top:126px;width:641px;height:2px;background:var(--brand-red)}
.plans{position:absolute;left:61px;top:165px;width:1079px;height:706px;border:1px solid var(--panel-edge);border-radius:14px;overflow:hidden;
  background:radial-gradient(ellipse 60% 55% at 62% 55%,#ffffff 0%,#f1f1f1 55%,#e6e6e6 100%)}
.corner{position:absolute;left:0;top:0}
.plans-head{position:absolute;left:0;top:0;width:100%;height:122px;border-bottom:1px solid var(--rule)}
.services-label{position:absolute;left:26px;top:77px;font-weight:800;font-size:26px;letter-spacing:7px;color:var(--brand-red)}
.plan{position:absolute;top:16px;width:258px;text-align:center}
.plan-security{left:523px}
.plan-essentials{left:804px}
.plan-name{display:flex;align-items:center;justify-content:center;gap:8px;height:46px;font-weight:800;font-size:23px}
.plan-name .light{color:var(--brand-grey)}
.plan-name .strong{color:var(--brand-red)}
.price{margin-top:13px;height:26px;line-height:26px;color:#fff;font-weight:800;font-size:17px}
.plan-security .price{background:var(--brand-red)}
.plan-essentials .price{background:var(--brand-grey)}
.head-divider{position:absolute;left:793px;top:14px;width:2px;height:90px;background:var(--brand-red)}
.col-divider{position:absolute;top:122px;bottom:0;width:1px;background:var(--rule)}
.col-divider.first{left:506px}
.col-divider.second{left:793px}
.rows{position:absolute;left:27px;top:122px;width:1034px;list-style:none}
.row{display:grid;grid-template-columns:479px 287px 268px;height:32.4px;align-items:center;border-bottom:2px dotted #7d7e81}
.row:last-child{border-bottom:none}
.service{font-weight:500;font-size:18.5px;letter-spacing:-.1px;white-space:nowrap}
.cell{display:flex;justify-content:center;align-items:center}
.cell.security{padding-right:0}
.cell.essentials{padding-left:0}
.avail{font-weight:600;font-size:13.5px;letter-spacing:3px;color:#555}
.tick{width:20px;height:18px}
.tick-red{stroke:var(--brand-red)}
.tick-grey{stroke:var(--tick-grey)}
.pricing-note{position:absolute;right:60px;top:882px;font-weight:700;font-size:14.5px;letter-spacing:2.6px;color:var(--brand-red)}
</style>
</head>
<body>
<main class="sheet">
  <div class="brand"><span class="brand-dot"></span><span class="brand-name">BQM</span></div>
  <div class="brand-tag">bqumesh network services</div>

  <header class="title">
    <div class="title-box">BQM</div>
    <h1 class="title-text">SUPPORT PLANS</h1>
  </header>
  <div class="title-rule"></div>

  <section class="plans">
    <svg class="corner" width="110" height="70" viewBox="0 0 110 70" aria-hidden="true">
      <path d="M0 0 H101 Q40 18 0 63 Z" fill="#6d6e72"/>
    </svg>
    <div class="plans-head">
      <div class="services-label">SERVICES</div>
      <div class="plan plan-security">
        <div class="plan-name">
          <svg width="36" height="42" viewBox="0 0 36 42" aria-hidden="true">
            <path d="M18 1 L34 6 V20 C34 31 26 38 18 41 C10 38 2 31 2 20 V6 Z" fill="#9b2424"/>
            <circle cx="18" cy="20" r="9" fill="#6d6e72" stroke="#fff" stroke-width="2"/>
            <path d="M18 15 V25 M13 20 H23" stroke="#fff" stroke-width="2.6"/>
          </svg>
          <span><span class="light">SECURITY</span> <span class="strong">Plus</span></span>
        </div>
        <div class="price">$75.00</div>
      </div>
      <div class="head-divider"></div>
      <div class="plan plan-essentials">
        <div class="plan-name">
          <svg width="44" height="42" viewBox="0 0 44 42" aria-hidden="true">
            <rect x="2" y="8" width="40" height="24" rx="2" fill="#9b2424"/>
            <rect x="2" y="28" width="40" height="4" fill="#c9c9c9"/>
            <rect x="19" y="32" width="6" height="5" fill="#6d6e72"/>
            <rect x="13" y="37" width="18" height="3" fill="#6d6e72"/>
            <circle cx="22" cy="18" r="6" fill="none" stroke="#fff" stroke-width="2.5" stroke-dasharray="3 2"/>
            <circle cx="8" cy="6" r="4" fill="none" stroke="#6d6e72" stroke-width="2" stroke-dasharray="2.5 1.5"/>
          </svg>
          <span><span class="light">IT</span> <span class="strong">Essentials</span></span>
        </div>
        <div class="price">$55.00 Per PC</div>
      </div>
    </div>
    <div class="col-divider first"></div>
    <div class="col-divider second"></div>

    <svg width="0" height="0" style="position:absolute" aria-hidden="true">
      <defs><path id="tick" d="M2 9 L8 15 L18 2" fill="none" stroke-width="3.2" stroke-linecap="round" stroke-linejoin="round"/></defs>
    </svg>

    <ul class="rows">
      <li class="row"><span class="service">Unlimited US bases Remote Help Desk Support</span><span class="cell security"><svg class="tick tick-red"><use href="#tick"/></svg></span><span class="cell essentials"><svg class="tick tick-grey"><use href="#tick"/></svg></span></li>
      <li class="row"><span class="service">Unlimited On-Site Support</span><span class="cell security"><svg class="tick tick-red"><use href="#tick"/></svg></span><span class="cell essentials"><span class="avail">Available</span></span></li>
      <li class="row"><span class="service">Advanced Cybersecurity and Threat Hunting</span><span class="cell security"><svg class="tick tick-red"><use href="#tick"/></svg></span><span class="cell essentials"><span class="avail">Available</span></span></li>
      <li class="row"><span class="service">Managed Antivirus Protection</span><span class="cell security"><svg class="tick tick-red"><use href="#tick"/></svg></span><span class="cell essentials"><svg class="tick tick-grey"><use href="#tick"/></svg></span></li>
      <li class="row"><span class="service">Multifactor Authentication Powered by Keyvora</span><span class="cell security"><svg class="tick tick-red"><use href="#tick"/></svg></span><span class="cell essentials"><span class="avail">Available</span></span></li>
      <li class="row"><span class="service">Cyber Security Awareness Training</span><span class="cell security"><svg class="tick tick-red"><use href="#tick"/></svg></span><span class="cell essentials"><span class="avail">Available</span></span></li>
      <li class="row"><span class="service">Enhanced Span Filtering</span><span class="cell security"><svg class="tick tick-red"><use href="#tick"/></svg></span><span class="cell essentials"><span class="avail">Available</span></span></li>
      <li class="row"><span class="service">Internet Content Filtering</span><span class="cell security"><svg class="tick tick-red"><use href="#tick"/></svg></span><span class="cell essentials"><span class="avail">Available</span></span></li>
      <li class="row"><span class="service">Proactive Security and System Monitoring</span><span class="cell security"><svg class="tick tick-red"><use href="#tick"/></svg></span><span class="cell essentials"><svg class="tick tick-grey"><use href="#tick"/></svg></span></li>
      <li class="row"><span class="service">Security and Vulnerability patching</span><span class="cell security"><svg class="tick tick-red"><use href="#tick"/></svg></span><span class="cell essentials"><svg class="tick tick-grey"><use href="#tick"/></svg></span></li>
      <li class="row"><span class="service">Backup and disaster recovery</span><span class="cell security"><svg class="tick tick-red"><use href="#tick"/></svg></span><span class="cell essentials"><svg class="tick tick-grey"><use href="#tick"/></svg></span></li>
      <li class="row"><span class="service">Network Management and Administration</span><span class="cell security"><svg class="tick tick-red"><use href="#tick"/></svg></span><span class="cell essentials"><svg class="tick tick-grey"><use href="#tick"/></svg></span></li>
      <li class="row"><span class="service">Nimbusoft Office Suite Administration and Configuration</span><span class="cell security"><svg class="tick tick-red"><use href="#tick"/></svg></span><span class="cell essentials"><svg class="tick tick-grey"><use href="#tick"/></svg></span></li>
      <li class="row"><span class="service">Nimbusoft Cloud Administration and Configuration</span><span class="cell security"><svg class="tick tick-red"><use href="#tick"/></svg></span><span class="cell essentials"><svg class="tick tick-grey"><use href="#tick"/></svg></span></li>
      <li class="row"><span class="service">Nimbusoft Desktop and Server Support</span><span class="cell security"><svg class="tick tick-red"><use href="#tick"/></svg></span><span class="cell essentials"><svg class="tick tick-grey"><use href="#tick"/></svg></span></li>
      <li class="row"><span class="service">Managed DNS</span><span class="cell security"><svg class="tick tick-red"><use href="#tick"/></svg></span><span class="cell essentials"><svg class="tick tick-grey"><use href="#tick"/></svg></span></li>
      <li class="row"><span class="service">Hardware and Software Procurement</span><span class="cell security"><svg class="tick tick-red"><use href="#tick"/></svg></span><span class="cell essentials"><svg class="tick tick-grey"><use href="#tick"/></svg></span></li>
      <li class="row"><span class="service">Assett Management</span><span class="cell security"><svg class="tick tick-red"><use href="#tick"/></svg></span><span class="cell essentials"><svg class="tick tick-grey"><use href="#tick"/></svg></span></li>
    </ul>
  </section>

  <p class="pricing-note">All Pricing is per month per PC</p>
</main>
</body>
</html>
```